Castastrophe General Contractor needs leave behind for sales

Will respond quickly to designer inquires
Fast winning selection
Will notify all of winning selection

Catastrophe Restoration General Contractor offering specialized services to the insurance industry. Sales meeting leave behind flyer for presentation to insurance agents. We would like for agents to refer policyholders to our company for complete residential and commercial restoration projects.

Some copy uploaded for reference. 5.5" x 8.5" approx - double sided color w/ sales business card reproduced on back side. Approved / Preferred Contractor for Coastwide, Vantora, RQBT & Selvo insurance companies.

Bramblecourt Company is a general contractor specialized in the restoration industry for both residential and commercial properties.
We have incorporated the best technology tools and partnered with a network of industry professionals across the country to provide the most efficient and comprehensive service available.
Website under construction: www.thebramblecourtcompany.example

Target Market(s)

Insurance Sale Agents

Industry/Entity Type

Residential

Requirements
Must have
• Coastwide, Vantora & RQBT & Hadley Vortan logos. Space to reproduce business card on back.. Looking for concept deign where we can work w/ local designer if necessary to finalize. Open to different sized flyer dependent on design.

```html
<!DOCTYPE html>
<html lang="en">
<head>
<meta charset="utf-8">
<title>Bramblecourt Company – Agent Leave-Behind Flyer</title>
<link href="https://fonts.googleapis.com/css2?family=Open+Sans:wght@400;600;700;800&display=swap" rel="stylesheet">
<style>
  :root {
    --bg: #e4e4e4;
    --paper: #ffffff;
    --umber: #5f514b;
    --umber-deep: #433833;
    --umber-soft: rgba(95, 81, 75, 0.88);
    --sepia-light: #d9d2cd;
    --sepia-mid: #a89a92;
    --ink: #3b3330;
    --grey-text: #8a817c;
    --brand: #1f5a8a;
  }
  * { box-sizing: border-box; margin: 0; padding: 0; }
  html, body { width: 1200px; height: 1000px; overflow: hidden; }
  body {
    background: var(--bg);
    font-family: "Open Sans", Arial, sans-serif;
    color: var(--ink);
    position: relative;
  }
  .flyer {
    position: absolute;
    left: 240px;
    width: 720px;
    height: 466px;
    background: var(--paper);
    overflow: hidden;
    box-shadow: 0 6px 18px rgba(0,0,0,0.18);
  }
  .flyer--front { top: 24px; }
  .flyer--back { top: 510px; }

  /* front */
  .house-art {
    position: absolute;
    background: linear-gradient(160deg, var(--sepia-light) 0%, var(--sepia-mid) 45%, var(--umber-deep) 75%, #f2efed 100%);
  }
  .flyer--front .house-art { left: 380px; top: 70px; width: 340px; height: 396px; }
  .title-box {
    position: absolute; left: 28px; top: 18px;
    border: 3px solid var(--ink);
    padding: 6px 12px 5px;
    line-height: 1;
    text-transform: uppercase;
    background: var(--paper);
    z-index: 1;
  }
  .title-box span { display: block; }
  .title-box .t-small { font-size: 19px; font-weight: 400; letter-spacing: 0.5px; }
  .title-box .t-big { font-size: 27px; font-weight: 800; letter-spacing: 0.5px; }
  .title-rule { position: absolute; left: 250px; right: 24px; top: 64px; height: 2px; background: var(--ink); }
  .site-line {
    position: absolute; right: 28px; top: 48px;
    font-size: 10px; letter-spacing: 2px; color: var(--ink);
  }
  .brand-mark {
    position: absolute; right: 28px; top: 84px;
    display: flex; align-items: center; gap: 6px;
    font-size: 13px; font-weight: 600; color: var(--brand);
    letter-spacing: 0.5px; text-transform: uppercase;
  }
  .brand-mark i { width: 10px; height: 10px; background: var(--brand); display: block; }
  .support-panel {
    position: absolute; left: 0; top: 108px; width: 500px; height: 232px;
    background: var(--umber-soft);
    color: #fff;
    padding: 12px 22px;
  }
  .support-panel h2 { font-size: 15px; font-weight: 700; line-height: 1.25; }
  .support-panel h3 { font-size: 14px; font-weight: 700; margin-top: 6px; }
  .service-list { list-style: none; font-size: 12.5px; line-height: 1.3; }
  .service-list li::before { content: "• "; }
  .support-body { display: flex; gap: 18px; margin-top: 10px; }
  .benefits { width: 140px; flex: none; display: flex; flex-direction: column; gap: 8px; }
  .benefit { display: flex; align-items: center; gap: 7px; font-size: 8px; font-weight: 600; line-height: 1.2; }
  .benefit svg { flex: none; }
  .fine-points { list-style: none; font-size: 8px; line-height: 1.5; opacity: 0.9; padding-top: 4px; }
  .fine-points li::before { content: "• "; }
  .carrier-row {
    position: absolute; left: 18px; top: 356px; width: 350px;
    display: flex; flex-wrap: wrap; align-items: center; gap: 10px 12px;
    font-size: 11px; font-weight: 700; color: var(--ink);
  }
  .carrier { display: flex; align-items: center; gap: 5px; white-space: nowrap; }
  .carrier i { width: 10px; height: 10px; border: 2px solid var(--ink); display: block; flex: none; }
  .seal { width: 28px; height: 28px; border-radius: 50%; background: var(--umber); flex: none; }
  .seal--sq { border-radius: 3px; width: 26px; height: 26px; background: var(--sepia-mid); }
  .carrier--preferred { text-transform: uppercase; font-size: 10px; line-height: 1.1; }

  /* back */
  .flyer--back .house-art { left: 200px; top: 100px; width: 520px; height: 366px;
    background: linear-gradient(150deg, #f4f1ef 0%, var(--sepia-light) 25%, var(--sepia-mid) 55%, var(--umber-deep) 80%, #ece8e5 100%); }
  .intro {
    position: absolute; left: 64px; top: 26px; width: 330px;
    font-size: 10px; line-height: 1.45; color: var(--grey-text);
  }
  .vertical-site {
    position: absolute; left: 24px; bottom: 34px;
    writing-mode: vertical-rl; transform: rotate(180deg);
    font-size: 12px; letter-spacing: 4px; color: var(--ink); white-space: nowrap;
  }
  .card-disc {
    position: absolute; left: 300px; top: 130px; width: 230px; height: 230px;
    border-radius: 50%; background: rgba(67, 56, 51, 0.85);
    color: #fff; display: flex; flex-direction: column; align-items: center; justify-content: center;
    text-align: center; gap: 8px;
  }
  .card-disc .card-name { font-size: 13px; font-weight: 600; letter-spacing: 1px; text-transform: uppercase; display: flex; align-items: center; gap: 6px; white-space: nowrap; }
  .card-disc .card-name i { width: 9px; height: 9px; background: #fff; display: block; flex: none; }
  .card-disc .card-contact { font-size: 10px; line-height: 1.5; letter-spacing: 0.5px; }
</style>
</head>
<body>

<section class="flyer flyer--front" aria-label="Flyer front">
  <div class="house-art" role="img" aria-label="Sepia 3D cutaway illustration of a house over architectural blueprints"></div>

  <div class="title-rule"></div>
  <div class="title-box">
    <span class="t-small">Your National</span>
    <span class="t-big">Restoration</span>
    <span class="t-small">Contractor</span>
  </div>
  <div class="site-line">www.thebramblecourtcompany.example</div>
  <div class="brand-mark"><i></i>Bramblecourt Company</div>

  <div class="support-panel">
    <h2>Preferred Contractor Agent Support<br>Providing claims support during and after a CAT event</h2>
    <h3>Agent Support Services</h3>
    <ul class="service-list">
      <li>Guaranteed next day inspections from time of notification</li>
      <li>Damage status reporting directly back to Agent</li>
      <li>Assist policy holder in filing claim to CAT desk</li>
    </ul>
    <div class="support-body">
      <div class="benefits">
        <div class="benefit">
          <svg width="18" height="18" viewBox="0 0 18 18"><path d="M2 8h3v8H2zM6 8l3-6c1.5 0 2 1 1.7 2.5L10 7h5c1 0 1.6 1 1.3 2l-1.6 5.5c-.3.9-1 1.5-2 1.5H6z" fill="#fff"/></svg>
          <span>Greater Satisfaction,<br>Increased Retention</span>
        </div>
        <div class="benefit">
          <svg width="18" height="18" viewBox="0 0 18 18"><circle cx="6" cy="9" r="4" fill="none" stroke="#fff" stroke-width="2"/><circle cx="13" cy="7" r="3" fill="none" stroke="#fff" stroke-width="2"/></svg>
          <span>Enhanced Efficiency</span>
        </div>
        <div class="benefit">
          <svg width="18" height="18" viewBox="0 0 18 18"><circle cx="9" cy="9" r="7" fill="none" stroke="#fff" stroke-width="2"/><path d="M5.5 9l2.5 2.5 4.5-5" fill="none" stroke="#fff" stroke-width="2"/></svg>
          <span>Increased Quality Control</span>
        </div>
      </div>
      <ul class="fine-points">
        <li>Pre-screened and credentialed by leading insurance carriers</li>
        <li>Standardized estimating aligned with carrier guidelines</li>
        <li>Background-checked crews on every residential project</li>
      </ul>
    </div>
  </div>

  <div class="carrier-row">
    <span class="carrier"><i></i>Coastwide</span>
    <span class="seal seal--sq"></span>
    <span class="carrier">Vantora</span>
    <span class="carrier">RQBT</span>
    <span class="seal"></span>
    <span class="seal"></span>
    <span class="seal"></span>
    <span class="carrier">Selvo</span>
    <span class="carrier carrier--preferred"><i></i>Preferred Contractor<br>Hadley Vortan</span>
  </div>
</section>

<section class="flyer flyer--back" aria-label="Flyer back">
  <div class="house-art" role="img" aria-label="Sepia 3D cutaway illustration of a house laid over floor plan drawings"></div>

  <p class="intro">We are your best choice for complete restoration services. Bramblecourt Company is a General Contractor specialized in the restoration industry for both residential and commercial properties. With operations currently established across 12 states, we have incorporated the best technology tools and partnered with a network of industry professionals.</p>

  <div class="vertical-site">www.thebramblecourtcompany.example</div>

  <div class="card-disc">
    <div class="card-name"><i></i>Bramblecourt Company</div>
    <div class="card-contact">(555) 010-0420<br>info@bramblecourt.example</div>
  </div>
</section>

</body>
</html>
```